Company's Core Values to be on our Office Walls

We are a biotechnology consulting company in Massachusetts with about 40 employees. Please check out velmora.com for our look and more information on our business.

We have 4 core values in the company which we would like to display in our office. (Could be on our walls, could be placed in our website, could be placed anywhere. - We would like a multi-use for this graphic but PRIMARILY on our walls.)
No measurements involved yet, hence we'd like the source file to enable us to stretch the graphics. What's important is to see the designs in this contest.

Design: Looking for a wall display - decal, glass board, vinyl (we're open)
- of our Core Values to have in our reception. We want a Double-Helix
incorporated as the core values are "in our DNA" like the one attached
(would like to see some designs with the exact photo and some used as
inspiration for a unique creative design). Open to various sizes, we have a
few different walls we could place them on.

We are looking for a creative Core Value display to have in our new office. We want a sleek, out of the box design!

Velmora's 4 Core Values are:
> Put Others First
> Have the Courage to Take Action
> Take Personal Responsibility
> Have fun!
***We welcome any infographics per core value. We are open to your creativity!

**WE WANT THE ACTUAL CORE VALUES ON DISPLAY**
We already have a brand (attached).
Need our actual values on display in office.
We want the actual values on the wall, our logo can be incorporated but not
necessarily.

Overview of company: Young consulting firm for biotech and pharmaceuticals
in the Greater Boston area. We are service based, our employees are
engineers and specialists that work on our clients site. Company was
established in 2010, we moved into our New England office 3 months ago!

Colors: Our main color is blue but we also use orange, green, purple, and
teal. See velmora.com for our colors.

Target Market(s)

New Hires and Clients - We want to impress them!
Employees and clients - we want employees inspired by the core
values and clients to be impressed by them/separate us from the competition.

Industry/Entity Type

Biotechnology

Font styles to use
Sans Serif

Colors

Designer to choose colors to be used in the design.

Requirements
Must have
• Creativity!
• Some sort of tie to science/biotech
• Color - Blue is our company color but would like others as well. See website for brand colors.

```html
<!DOCTYPE html>
<html lang="en">
<head>
<meta charset="utf-8">
<title>Velmora Core Values</title>
<link rel="stylesheet" href="https://fonts.googleapis.com/css2?family=Questrial&display=swap">
<style>
  :root {
    --wall-blue: #04578a;
    --wall-blue-deep: #034a78;
    --pattern-tone: #0a4d79;
    --glow-blue: #0b8cc6;
    --ring-blue: #0a6fa6;
    --ring-dark: #0c5686;
    --core-navy: #13405f;
    --value-white: #ffffff;
  }
  html, body {
    margin: 0;
    padding: 0;
    overflow: hidden;
    background: var(--wall-blue);
  }
  .values-wall {
    position: relative;
    width: 1200px;
    height: 700px;
    overflow: hidden;
    background: var(--wall-blue);
  }
  .molecule-pattern {
    position: absolute;
    inset: 0;
    background: radial-gradient(ellipse at 50% 50%, var(--wall-blue) 0%, var(--wall-blue) 45%, var(--pattern-tone) 100%);
  }
  .values-art {
    position: absolute;
    inset: 0;
    width: 1200px;
    height: 700px;
  }
  .value-text {
    font-family: "Questrial", "Century Gothic", sans-serif;
    fill: var(--value-white);
    text-transform: uppercase;
  }
  .value-major { font-size: 46px; letter-spacing: 3px; }
  .value-courage { font-size: 40px; letter-spacing: 2px; }
  .value-responsibility { font-size: 26px; letter-spacing: 2px; }
  .value-fun { font-size: 42px; letter-spacing: 3px; }
  .company-name {
    font-family: "Questrial", "Century Gothic", sans-serif;
    font-size: 50px;
    fill: var(--value-white);
    letter-spacing: 1px;
  }
</style>
</head>
<body>
<main class="values-wall">
  <div class="molecule-pattern" role="img" aria-label="Faint pattern of linked molecule shapes across the blue wall"></div>

  <svg class="values-art" viewBox="0 0 1247 728" preserveAspectRatio="none" aria-labelledby="values-title">
    <title id="values-title">Velmora core values arranged around the company name</title>
    <defs>
      <radialGradient id="core-glow" cx="648" cy="370" r="330" gradientUnits="userSpaceOnUse">
        <stop offset="0" stop-color="var(--glow-blue)"/>
        <stop offset="0.55" stop-color="var(--ring-blue)" stop-opacity="0.8"/>
        <stop offset="1" stop-color="var(--wall-blue)" stop-opacity="0"/>
      </radialGradient>

      <path id="arc-others-first" d="M329.2,342.1 A320,320 0 0 1 757.4,69.3"/>
      <path id="arc-responsibility" d="M316.6,619.7 A415,415 0 0 1 392.5,43"/>
      <path id="arc-courage" d="M410.5,569.3 A310,310 0 1 0 803,101.5"/>
      <path id="arc-fun" d="M1008.4,622.4 A440,440 0 0 0 1081.3,293.6"/>
    </defs>

    <g class="core-rings">
      <circle cx="648" cy="370" r="330" fill="url(#core-glow)"/>
      <circle cx="648" cy="370" r="270" fill="none" stroke="var(--ring-blue)" stroke-opacity="0.45" stroke-width="14"/>
      <circle cx="648" cy="370" r="235" fill="none" stroke="var(--ring-blue)" stroke-opacity="0.5" stroke-width="12"/>
      <circle cx="648" cy="370" r="205" fill="none" stroke="var(--glow-blue)" stroke-opacity="0.5" stroke-width="10"/>
      <circle cx="648" cy="370" r="168" fill="none" stroke="var(--ring-dark)" stroke-width="12"/>
      <circle cx="648" cy="370" r="150" fill="var(--core-navy)"/>
    </g>

    <text class="company-name" x="648" y="388" text-anchor="middle">Velmora</text>

    <text class="value-text value-major">
      <textPath href="#arc-others-first" textLength="520" lengthAdjust="spacing">Put others first</textPath>
    </text>
    <text class="value-text value-responsibility">
      <textPath href="#arc-responsibility" textLength="595" lengthAdjust="spacing">Take personal responsibility</textPath>
    </text>
    <text class="value-text value-courage">
      <textPath href="#arc-courage" startOffset="20" textLength="900" lengthAdjust="spacing">Have the courage to take action</textPath>
    </text>
    <text class="value-text value-fun">
      <textPath href="#arc-fun" startOffset="6" textLength="285" lengthAdjust="spacing">Have fun!</textPath>
    </text>
  </svg>
</main>
</body>
</html>
```